Sprinkles & Tails 2nd Annual Fundraiser

I am a Realtor sponsoring the 2nd annual fundraiser on behalf of Allies of Harlow Vale Animal Haven. Like the flyer to be professional yet fun and inviting. Please see the attached file below. The 1st annual flyer was fun but not as professional, modern or inviting as I would have liked it to be.
Target Market(s)
Dog lovers in Ponte Vedra, Ponte Vedra Beach and Nocatee Florida
Logo Text
Needed
Font styles to use
Other font styles liked:
- Font that fits the style of the fundraiser
Colors
886aae
abd036
Requirements
Must have
- Please see the attached flyer and photos.
- This will be the 2nd Annual on Saturday, April 27, 2019 from 10AM - 1PM. Same location: Kendrick Realty, 418 Tillbrook Ave. Ponte Vedra FL 32075

```html
<!DOCTYPE html>
<html lang="en">
<head>
<meta charset="utf-8">
<title>Sprinkles &amp; Tails – 2nd Annual Doggie Wash</title>
<link rel="stylesheet" href="https://fonts.googleapis.com/css2?family=Fredoka:wght@500;600;700&family=Playfair+Display:ital,wght@1,500&family=Oswald:wght@500&family=Open+Sans:wght@400;600&display=swap">
<style>
  :root {
    --purple: #886aae;
    --lime: #abd036;
    --lime-deep: #8cb41f;
    --navy: #3b4fa0;
    --paper: #f5f5f3;
    --ink: #2a2a2a;
    --wood: #c9a66b;
    --plank: #8b3e1d;
    --gold: #c29a2c;
    --sign-text: #5a1e12;
  }
  * { box-sizing: border-box; margin: 0; padding: 0; }
  html, body { width: 838px; height: 1200px; overflow: hidden; background: var(--paper); }
  .flyer {
    position: relative; width: 838px; height: 1200px;
    background: var(--paper); overflow: hidden;
    font-family: "Open Sans", Arial, sans-serif; color: var(--ink);
  }
  .photo { position: absolute; }
  .photo--groomed-dog {
    left: 79px; top: 72px; width: 310px; height: 290px;
    border-radius: 110px 0 0 110px;
    background: linear-gradient(135deg, #5b5f64, #a9a39a 55%, #d3c2a8);
    box-shadow: -24px -22px 0 0 var(--lime);
  }
  .photo--volunteer-dog {
    left: 403px; top: 40px; width: 340px; height: 322px;
    border-radius: 0 110px 0 110px;
    background: linear-gradient(140deg, #2b2b2b 0 30%, #c48a4e 55%, #8d7a6a);
  }
  .photo--wash-station {
    left: 141px; top: 374px; width: 248px; height: 227px;
    border-radius: 90px 0 0 90px;
    background: linear-gradient(160deg, #9a8a78, #6e6660 50%, #b7aea3);
  }

  .headline { position: absolute; left: 408px; top: 366px; font-family: "Fredoka", sans-serif; font-weight: 700; line-height: 1; }
  .headline__edition { display: block; color: var(--lime); font-size: 52px; }
  .headline__name { display: block; color: var(--purple); font-size: 60px; margin-top: 6px; letter-spacing: -1px; }
  .headline__name--big { font-size: 110px; margin-top: -2px; letter-spacing: -3px; }
  .tagline { position: absolute; left: 410px; top: 594px; font-family: "Fredoka", sans-serif; font-weight: 700; color: var(--lime-deep); font-size: 23px; }
  .subline { position: absolute; left: 411px; top: 630px; font-family: "Playfair Display", serif; font-style: italic; font-size: 20px; color: var(--ink); }

  .highlights { position: absolute; left: 428px; top: 671px; list-style: none; font-family: "Fredoka", sans-serif; font-weight: 700; font-size: 20px; }
  .highlights li { height: 33px; display: flex; align-items: center; gap: 10px; }
  .highlights li:nth-child(odd) { color: var(--navy); }
  .highlights li:nth-child(even) { color: var(--lime-deep); }
  .highlights svg { width: 15px; height: 15px; fill: var(--purple); flex: none; }

  .lawn {
    position: absolute; left: 0; top: 878px; width: 838px; height: 192px;
    background: linear-gradient(180deg, #7cbc3a, #4f9a26 60%, #3f8420);
  }

  .event-panel {
    position: absolute; left: 12px; top: 624px; width: 386px; height: 246px;
    background: var(--wood); border-radius: 4px;
  }
  .event-panel__day { position: absolute; left: 42px; top: 16px; font-family: "Fredoka", sans-serif; font-weight: 700; font-size: 30px; color: var(--lime); }
  .event-panel__date { position: absolute; left: 40px; top: 50px; font-family: "Fredoka", sans-serif; font-weight: 700; font-size: 58px; color: #fff; -webkit-text-stroke: 2px #1d1d1d; letter-spacing: -1px; line-height: 1; }
  .event-panel__venue { position: absolute; left: 42px; top: 128px; font-family: "Oswald", sans-serif; font-size: 17px; line-height: 22px; color: var(--sign-text); text-transform: uppercase; }
  .event-panel__time { position: absolute; left: 232px; top: 128px; font-family: "Fredoka", sans-serif; font-weight: 700; font-size: 19px; color: var(--lime); -webkit-text-stroke: 1px #1d1d1d; }
  .event-panel__rain { position: absolute; left: 42px; top: 206px; font-size: 15px; font-weight: 600; color: #2b2218; }

  .mascot-area { position: absolute; left: 380px; top: 882px; width: 100px; height: 116px; background: #c79a68; border-radius: 6px; }

  .donate-panel {
    position: absolute; left: 540px; top: 912px; width: 282px; height: 100px;
    background: var(--plank); border-radius: 4px;
    text-align: center; color: #fff; font-family: "Oswald", sans-serif;
  }
  .donate-panel__lead { font-size: 18px; margin-top: 9px; }
  .donate-panel__url { font-size: 15px; margin-top: 2px; }
  .donate-panel__button { display: inline-block; margin-top: 6px; padding: 1px 22px; background: var(--lime); border-radius: 14px; font-family: "Fredoka", sans-serif; font-weight: 700; font-size: 15px; }

  .guidelines { position: absolute; left: 44px; top: 1010px; width: 480px; font-size: 15px; line-height: 21px; color: #fff; }

  .footer { position: absolute; left: 0; top: 1070px; width: 838px; height: 130px; background: #fff; border-top: 3px solid var(--lime); }
  .footer__support { position: absolute; left: 72px; top: 12px; font-family: "Playfair Display", serif; font-style: italic; font-size: 14px; }
  .partner-name { position: absolute; left: 56px; top: 38px; width: 128px; font-family: "Fredoka", sans-serif; font-weight: 600; font-size: 13px; line-height: 16px; color: var(--ink); text-align: center; }
  .contact { position: absolute; top: 30px; font-size: 12.5px; line-height: 16px; }
  .contact__name { font-family: "Fredoka", sans-serif; font-weight: 600; font-size: 19px; color: var(--gold); margin-bottom: 3px; }
  .contact--organizer { left: 196px; }
  .contact--realtor { left: 562px; }
  .realtor-name { position: absolute; left: 392px; top: 48px; font-family: "Fredoka", sans-serif; font-weight: 600; font-size: 19px; color: var(--navy); }
</style>
</head>
<body>
<main class="flyer">
  <div class="photo photo--groomed-dog" role="img" aria-label="Photo of a happy shaggy grey dog in a pink bandana at the wash sign"></div>
  <div class="photo photo--volunteer-dog" role="img" aria-label="Photo of a volunteer hugging a tan dog in a red harness beside the event chalkboard"></div>
  <div class="photo photo--wash-station" role="img" aria-label="Photo of volunteers washing a dog at the event"></div>

  <h1 class="headline">
    <span class="headline__edition">2nd Annual</span>
    <span class="headline__name">Sprinkles &amp;</span>
    <span class="headline__name headline__name--big">Tails</span>
  </h1>
  <p class="tagline">Doggie Wash Extravaganza</p>
  <p class="subline">A Family Fun Event for All Ages</p>

  <ul class="highlights">
    <li><svg viewBox="0 0 16 16"><circle cx="8" cy="11" r="4"/><circle cx="3" cy="6" r="2"/><circle cx="6.5" cy="3" r="2"/><circle cx="10.5" cy="3.5" r="2"/><circle cx="13.5" cy="7" r="2"/></svg>FREE Doggie Wash</li>
    <li><svg viewBox="0 0 16 16"><circle cx="8" cy="11" r="4"/><circle cx="3" cy="6" r="2"/><circle cx="6.5" cy="3" r="2"/><circle cx="10.5" cy="3.5" r="2"/><circle cx="13.5" cy="7" r="2"/></svg>Raffle Drawings</li>
    <li><svg viewBox="0 0 16 16"><circle cx="8" cy="11" r="4"/><circle cx="3" cy="6" r="2"/><circle cx="6.5" cy="3" r="2"/><circle cx="10.5" cy="3.5" r="2"/><circle cx="13.5" cy="7" r="2"/></svg>Food &amp; Beverages</li>
    <li><svg viewBox="0 0 16 16"><circle cx="8" cy="11" r="4"/><circle cx="3" cy="6" r="2"/><circle cx="6.5" cy="3" r="2"/><circle cx="10.5" cy="3.5" r="2"/><circle cx="13.5" cy="7" r="2"/></svg>Grand Prize</li>
    <li><svg viewBox="0 0 16 16"><circle cx="8" cy="11" r="4"/><circle cx="3" cy="6" r="2"/><circle cx="6.5" cy="3" r="2"/><circle cx="10.5" cy="3.5" r="2"/><circle cx="13.5" cy="7" r="2"/></svg>Vendors (FREE give-a-ways)</li>
    <li><svg viewBox="0 0 16 16"><circle cx="8" cy="11" r="4"/><circle cx="3" cy="6" r="2"/><circle cx="6.5" cy="3" r="2"/><circle cx="10.5" cy="3.5" r="2"/><circle cx="13.5" cy="7" r="2"/></svg>Donations Welcome</li>
  </ul>

  <div class="lawn" role="img" aria-label="Illustrated grassy lawn with wooden signposts"></div>

  <section class="event-panel" aria-label="Event date and location">
    <div class="event-panel__day">Saturday</div>
    <div class="event-panel__date">April 27th</div>
    <div class="event-panel__venue">Kendrick Realty<br>418 Tillbrook Ave.<br>Ponte Vedra FL 32075</div>
    <div class="event-panel__time">10 AM - 1 PM</div>
    <div class="event-panel__rain">(Rain date: Saturday, May 5th)</div>
  </section>

  <div class="mascot-area" role="img" aria-label="Cartoon puppy mascot sitting on the grass"></div>

  <section class="donate-panel">
    <div class="donate-panel__lead">TO MAKE A DONATION:</div>
    <div class="donate-panel__url">HTTPS://WWW.FUNDPAGE.ORG/AHVAH/</div>
    <div class="donate-panel__button">Donate</div>
  </section>

  <p class="guidelines">All domestic breeds from puppies to seniors invited. Please be sure Furry Fido is tolerant of other dogs, crowds and bathing.</p>

  <footer class="footer">
    <div class="footer__support">In Support of</div>
    <div class="partner-name">Allies of Harlow Vale Animal Haven</div>
    <div class="contact contact--organizer">
      <div class="contact__name">Dana Whitfield</div>
      AHVAH<br>904.555.0142<br>dana.whitfield@mailbox.net
    </div>
    <div class="realtor-name">Marlene Hayes</div>
    <div class="contact contact--realtor">
      <div class="contact__name">Marlene Hayes</div>
      Kendrick Realty Corp.<br>770.555.0198<br>marlenehayes@kendrickrealtycorp.com
    </div>
  </footer>
</main>
</body>
</html>
```